Pressfield Design for a Business Blog

We are running the finance blog kivo.net and want to renew our web page design. Thus, we need a new designed Pressfield theme containing an overview page, used on the front page and the start pages of the categories, and a single article view like on http://kivo.net/blog/coping-with-falling-dollar/ . The new look should be serious, should contain all elements of the current website, should look professional (no entertainment elements) and in light colors.
Updates

Reason: Due to some request, we've extended the deadline a few days.

Reason: Hello,

we received a comment that our budget is to low for  a complete Pressfield design including coding. Thus, we changed our requriement to psd design  only,  without coding.

Industry/Entity Type

Entertainment

Requirements
Must have
• * Light colors
* Two column layout
* Contain all elements of the current website www.kivo.net
Should not have
• * Too much colors
* Look to flashy

```html
<!DOCTYPE html>
<html lang="en">
<head>
<meta charset="utf-8">
<title>kivo.net – Finance Blog</title>
<link rel="stylesheet" href="https://fonts.googleapis.com/css2?family=Arimo:wght@400;700&family=Gelasio:wght@400;700&display=swap">
<style>
  :root{
    --page:#f3f3f1;
    --bar:#151515;
    --bar-edge:#2c2c2c;
    --nav-active:#86b52a;
    --green:#6f9b22;
    --green-light:#c4e240;
    --green-deep:#7fb319;
    --card:#ffffff;
    --card-line:#e3e3df;
    --widget:#eeeeea;
    --widget-line:#dcdcd6;
    --text:#3b3b3b;
    --muted:#666;
    --ad:#3a3a3a;
  }
  *{box-sizing:border-box;margin:0;padding:0}
  html,body{width:865px;height:1200px;overflow:hidden}
  body{background:var(--page);font-family:"Arimo",Arial,sans-serif;color:var(--text);position:relative}
  .top-glow{position:absolute;left:0;top:32px;width:865px;height:90px;background:linear-gradient(#fff,var(--page))}

  .topbar{position:absolute;left:0;top:0;width:865px;height:32px;background:linear-gradient(#2a2a2a,var(--bar));border-bottom:1px solid var(--bar-edge)}
  .nav{position:absolute;left:209px;top:6px;display:flex;gap:4px;list-style:none}
  .nav li{font-size:7.6px;color:#fff;text-transform:uppercase;padding:4px 5px;border-radius:3px;letter-spacing:.1px}
  .nav li.active{background:var(--nav-active)}

  .banner{position:absolute;left:209px;top:44px;width:448px;height:108px;background:#fff;border:1px solid #ddd;padding:4px;box-shadow:0 4px 8px rgba(0,0,0,.12)}
  .banner-inner{position:relative;width:100%;height:100%;background:radial-gradient(circle at 40% 40%,var(--green-light),var(--green-deep) 85%);overflow:hidden}
  .brand{position:absolute;left:14px;top:12px;font-weight:700;font-size:22px;color:#1f2a0a;letter-spacing:-.5px}
  .slogan{position:absolute;left:14px;top:42px;font-weight:700;font-size:12px;line-height:13px;color:#fff;text-transform:uppercase}
  .tagline{position:absolute;left:14px;top:72px;font-size:8px;color:#fff}
  .banner-photo{position:absolute;right:4px;top:0;width:120px;height:100%;background:linear-gradient(90deg,rgba(150,190,60,0),#9c8a5a 35%,#6d6a3e)}

  .post{position:absolute;left:209px;width:293px;height:231px;background:var(--card);border:1px solid var(--card-line)}
  .post-meta{position:absolute;left:12px;right:12px;top:7px;height:14px;border-bottom:1px solid var(--card-line);font-size:5.6px;color:#444;display:flex;justify-content:space-between;align-items:center;padding-bottom:4px}
  .post-title{position:absolute;left:12px;top:26px;font-family:"Gelasio",Georgia,serif;font-size:14.5px;color:var(--green);font-weight:400}
  .post-thumb{position:absolute;left:13px;top:51px;width:148px;height:99px;border:1px solid #ccc;padding:2px;background:#fff}
  .post-thumb div{width:100%;height:100%;background:radial-gradient(circle,#5b6343,#343a24);display:flex;flex-direction:column;align-items:center;justify-content:center;color:#e8e8e0;font-weight:700;font-size:20px;line-height:25px}
  .post-thumb span{font-weight:400}
  .post-side{position:absolute;left:170px;top:49px;width:112px;font-size:5.8px;line-height:8.6px;color:#555}
  .post-side p+p{margin-top:4px}
  .post-body{position:absolute;left:12px;top:155px;width:270px;font-size:5.8px;line-height:8.6px;color:#555}
  .post-body p+p{margin-top:4px}
  .share{position:absolute;left:14px;top:209px;display:flex;gap:5px}
  .share i{display:block;width:11px;height:11px;border-radius:50%;border:1px solid #bbb}
  .read-more{position:absolute;right:18px;top:210px;font-size:5.6px;color:#555;border:1px solid #ccc;border-radius:6px;padding:2px 4px 2px 6px;background:linear-gradient(#fff,#eee);display:flex;align-items:center;gap:3px}
  .read-more b{width:6px;height:6px;border-radius:50%;background:#333;display:inline-block}

  .older{position:absolute;left:213px;top:1146px;font-size:6px;color:#444;text-decoration:underline}

  .sidebar{position:absolute;left:512px;top:169px;width:145px;display:flex;flex-direction:column;gap:10px}
  .search{position:relative;height:16px;border:1px solid #ccc;border-radius:9px;background:#fff;font-size:6px;color:#999;padding:4px 10px;box-shadow:inset 0 1px 2px rgba(0,0,0,.1);margin-bottom:2px}
  .search svg{position:absolute;right:7px;top:3px}

  .widget{background:var(--widget);border:1px solid var(--widget-line);padding:8px 9px}
  .widget h3{font-family:"Gelasio",Georgia,serif;font-weight:400;font-size:12px;line-height:15px;color:#222;padding-bottom:3px;border-bottom:1px solid #d5d5cf;margin-bottom:5px}
  .widget ul{list-style:none}
  .widget li{font-size:6.2px;color:#555;line-height:8px;padding:2px 0 2px 11px;position:relative}
  .widget li::before{content:"";position:absolute;left:1px;top:3px;width:6px;height:6px;border-radius:50%;background:#d3d3cc;border:1px solid #bdbdb5}
  .ads{display:grid;grid-template-columns:60px 60px;gap:4px 6px;padding:2px 1px}
  .ad{height:60px;background:radial-gradient(circle,#555,var(--ad));border:1px solid #222;color:#fff;font-weight:700;font-size:8px;display:flex;align-items:center;justify-content:center;text-align:center;line-height:10px}

  .footer{position:absolute;left:0;top:1176px;width:865px;height:24px;background:var(--bar);border-top:3px solid #ccc;font-size:6.4px;color:#ddd}
  .footer .left{position:absolute;left:210px;top:6px}
  .footer .right{position:absolute;right:209px;top:6px}
</style>
</head>
<body>
<div class="top-glow"></div>

<header class="topbar">
  <ul class="nav">
    <li class="active">Home</li><li>Finance</li><li>Economy</li><li>Resources</li><li>Personal Saving</li><li>Make Money</li><li>Miscellaneous</li><li>Uncategorized</li>
  </ul>
</header>

<section class="banner">
  <div class="banner-inner">
    <div class="brand">KIVO.NET</div>
    <div class="slogan">Is all about achieving your<br>financial goals</div>
    <div class="tagline">We not only prove our results...we can guarantee them too!</div>
    <div class="banner-photo" role="img" aria-label="Photo of a woman beside banknotes hanging on a line"></div>
  </div>
</section>

<main>
  <article class="post" style="top:171px">
    <div class="post-meta"><span>◷ December 22nd, 2008 | Edit</span><span>▭ 0 Comments</span></div>
    <h2 class="post-title">Sample Post No : 1</h2>
    <div class="post-thumb"><div>SAMPLE<span>POST</span></div></div>
    <div class="post-side"><p>Lorem ipsum dolor sit amet, consectetur adipiscing elit. Integer sed neque.</p><p>Curabitur neque. Duis a massa. Nam quis nulla eu nisl pulvinar bibendum. Sed Elit euismod, enim vel porttitor elementum, odio nunc facilisis nunc, eget sagittis liber massa quis mauris. Vivamus quis est vitae magna feugiat commodo. Pellentesque is quis mauris. Suspendisse eu velit et tellus euismod rutrum. Nulla convallis neque aer risus. Aliquam pretium, purus et interdu.</p></div>
    <div class="post-body"><p>Fusce quam mi, tincidunt vel, fermentum a, cursus ac, leo. Maecenas sollicitudin tortor nec magnagtd praesent tellus. Suspendisse venenatis libero a nisl. Mauris scelerisque. Etiam laoreet ante id elit.</p><p>Integer laoreet. In id dolor a tellus vestibulum aliquet. Quisque in turpis. Nulla facilisi. Morbi felis. Ut qua leo, dapibus vitae, pulvinar ut, vehicula blandit, dui.</p></div>
    <div class="share"><i style="background:#5aa83a"></i><i style="background:#2d4d9a"></i><i style="background:#ddd"></i><i style="background:#ccc"></i><i style="background:#4aa86b"></i></div>
    <div class="read-more">Read More <b></b></div>
  </article>

  <article class="post" style="top:415px">
    <div class="post-meta"><span>◷ December 22nd, 2008 | Edit</span><span>▭ 0 Comments</span></div>
    <h2 class="post-title">Sample Post No : 1</h2>
    <div class="post-thumb"><div>SAMPLE<span>POST</span></div></div>
    <div class="post-side"><p>Lorem ipsum dolor sit amet, consectetur adipiscing elit. Integer sed neque.</p><p>Curabitur neque. Duis a massa. Nam quis nulla eu nisl pulvinar bibendum. Sed Elit euismod, enim vel porttitor elementum, odio nunc facilisis nunc, eget sagittis liber massa quis mauris. Vivamus quis est vitae magna feugiat commodo. Pellentesque is quis mauris. Suspendisse eu velit et tellus euismod rutrum. Nulla convallis neque aer risus. Aliquam pretium, purus et interdu.</p></div>
    <div class="post-body"><p>Fusce quam mi, tincidunt vel, fermentum a, cursus ac, leo. Maecenas sollicitudin tortor nec magnagtd praesent tellus. Suspendisse venenatis libero a nisl. Mauris scelerisque. Etiam laoreet ante id elit.</p><p>Integer laoreet. In id dolor a tellus vestibulum aliquet. Quisque in turpis. Nulla facilisi. Morbi felis. Ut qua leo, dapibus vitae, pulvinar ut, vehicula blandit, dui.</p></div>
    <div class="share"><i style="background:#5aa83a"></i><i style="background:#2d4d9a"></i><i style="background:#ddd"></i><i style="background:#ccc"></i><i style="background:#4aa86b"></i></div>
    <div class="read-more">Read More <b></b></div>
  </article>

  <article class="post" style="top:659px">
    <div class="post-meta"><span>◷ December 22nd, 2008 | Edit</span><span>▭ 0 Comments</span></div>
    <h2 class="post-title">Sample Post No : 1</h2>
    <div class="post-thumb"><div>SAMPLE<span>POST</span></div></div>
    <div class="post-side"><p>Lorem ipsum dolor sit amet, consectetur adipiscing elit. Integer sed neque.</p><p>Curabitur neque. Duis a massa. Nam quis nulla eu nisl pulvinar bibendum. Sed Elit euismod, enim vel porttitor elementum, odio nunc facilisis nunc, eget sagittis liber massa quis mauris. Vivamus quis est vitae magna feugiat commodo. Pellentesque is quis mauris. Suspendisse eu velit et tellus euismod rutrum. Nulla convallis neque aer risus. Aliquam pretium, purus et interdu.</p></div>
    <div class="post-body"><p>Fusce quam mi, tincidunt vel, fermentum a, cursus ac, leo. Maecenas sollicitudin tortor nec magnagtd praesent tellus. Suspendisse venenatis libero a nisl. Mauris scelerisque. Etiam laoreet ante id elit.</p><p>Integer laoreet. In id dolor a tellus vestibulum aliquet. Quisque in turpis. Nulla facilisi. Morbi felis. Ut qua leo, dapibus vitae, pulvinar ut, vehicula blandit, dui.</p></div>
    <div class="share"><i style="background:#5aa83a"></i><i style="background:#2d4d9a"></i><i style="background:#ddd"></i><i style="background:#ccc"></i><i style="background:#4aa86b"></i></div>
    <div class="read-more">Read More <b></b></div>
  </article>

  <article class="post" style="top:903px">
    <div class="post-meta"><span>◷ December 22nd, 2008 | Edit</span><span>▭ 0 Comments</span></div>
    <h2 class="post-title">Sample Post No : 1</h2>
    <div class="post-thumb"><div>SAMPLE<span>POST</span></div></div>
    <div class="post-side"><p>Lorem ipsum dolor sit amet, consectetur adipiscing elit. Integer sed neque.</p><p>Curabitur neque. Duis a massa. Nam quis nulla eu nisl pulvinar bibendum. Sed Elit euismod, enim vel porttitor elementum, odio nunc facilisis nunc, eget sagittis liber massa quis mauris. Vivamus quis est vitae magna feugiat commodo. Pellentesque is quis mauris. Suspendisse eu velit et tellus euismod rutrum. Nulla convallis neque aer risus. Aliquam pretium, purus et interdu.</p></div>
    <div class="post-body"><p>Fusce quam mi, tincidunt vel, fermentum a, cursus ac, leo. Maecenas sollicitudin tortor nec magnagtd praesent tellus. Suspendisse venenatis libero a nisl. Mauris scelerisque. Etiam laoreet ante id elit.</p><p>Integer laoreet. In id dolor a tellus vestibulum aliquet. Quisque in turpis. Nulla facilisi. Morbi felis. Ut qua leo, dapibus vitae, pulvinar ut, vehicula blandit, dui.</p></div>
    <div class="share"><i style="background:#5aa83a"></i><i style="background:#2d4d9a"></i><i style="background:#ddd"></i><i style="background:#ccc"></i><i style="background:#4aa86b"></i></div>
    <div class="read-more">Read More <b></b></div>
  </article>

  <div class="older">« Older Entries</div>
</main>

<aside class="sidebar">
  <div class="search">search...
    <svg width="11" height="10" viewBox="0 0 11 10"><circle cx="4" cy="4" r="3" fill="none" stroke="#888" stroke-width="1.4"/><line x1="6.3" y1="6.3" x2="10" y2="9.5" stroke="#888" stroke-width="1.8"/></svg>
  </div>

  <div class="widget" style="min-height:144px">
    <div class="ads">
      <div class="ad">Advertise<br>Here</div><div class="ad">Advertise<br>Here</div>
      <div class="ad">Advertise<br>Here</div><div class="ad">Advertise<br>Here</div>
    </div>
  </div>

  <div class="widget" style="min-height:123px">
    <h3>Categories</h3>
    <ul><li>Finance (38)</li><li>Economy (31)</li><li>Resources (44)</li><li>Personal Saving (45)</li><li>Make Money (13)</li><li>Miscellaneous (53)</li><li>Uncategorized (11)</li></ul>
  </div>

  <div class="widget" style="min-height:82px">
    <h3>Popular Posts</h3>
    <ul><li>Will You Inherit Your Parents' Debt?</li><li>Money Saving Quotes</li><li>Product Labels: More Than Meets The Eye</li></ul>
  </div>

  <div class="widget" style="min-height:99px">
    <h3>Recent Posts</h3>
    <ul><li>Money / Saving Jokes</li><li>Surviving the Euro Crisis</li><li>Coping With Falling Dollar</li><li>6 Secrets to Successful Saving</li><li>Something Old: Something New?</li></ul>
  </div>

  <div class="widget" style="min-height:147px">
    <h3>Archives</h3>
    <ul><li>June 2011</li><li>May 2011</li><li>April 2011</li><li>March 2011</li><li>February 2011</li><li>January 2011</li><li>December 2010</li><li>November 2010</li><li>October 2010</li></ul>
  </div>

  <div class="widget" style="min-height:174px">
    <h3>Tags</h3>
    <ul><li>financial planner</li><li>financial planning</li><li>financial planning process</li><li>frugal lifestyle</li><li>frugal living</li><li>overspending</li><li>personal saving</li><li>retirement</li><li>save money</li><li>unemployment</li><li>more tags</li></ul>
  </div>

  <div class="widget" style="min-height:46px">
    <h3>Blogroll</h3>
    <ul><li>Ledgerly.com</li></ul>
  </div>
</aside>

<footer class="footer">
  <div class="left">© 2011 <b>kivo.net</b> is proudly powered by Pressfield.</div>
  <div class="right"><b>Privacy Policy</b> | <b>Terms &amp; Conditions</b> Allrights reserved.</div>
</footer>
</body>
</html>
```